11 x 11 Flyer Design for Social Media - Reverse Mortgages

62 or older?

A Reverse Mortgage
could be
Your Road to Financial Freedom

* No Monthly Payments
* No Income Requirements
* No Credit Score Requirements
* No Loss of Ownership

Receive cash by lump sum, monthly installments or a line of credit!!

Call us today for a Free Consultation!!
(800) 471-2965

Bluegate Financial Services, Inc.
NMLS #318760
www.bluegatehome.com

```html
<!DOCTYPE html>
<html lang="en">
<head>
<meta charset="utf-8">
<title>Reverse Mortgages Flyer</title>
<link rel="stylesheet" href="https://fonts.googleapis.com/css2?family=Montserrat:wght@400;500;600;700;800&display=swap">
<style>
  :root {
    --blue: #2463ab;
    --gold: #bcaa45;
    --white: #ffffff;
    --backdrop: #e4e5e7;
    --photo-warm-a: #c9a58a;
    --photo-warm-b: #f3efec;
    --photo-dark-a: #4f4b3a;
    --photo-dark-b: #6e6a55;
    --photo-dark-c: #3d3a2f;
  }
  * { box-sizing: border-box; margin: 0; padding: 0; }
  html, body { width: 1200px; height: 600px; overflow: hidden; }
  body {
    background: var(--backdrop);
    font-family: "Montserrat", Arial, sans-serif;
    position: relative;
  }
  .flyer {
    position: absolute;
    left: 310px; top: 10px;
    width: 580px; height: 580px;
    background: var(--white);
    overflow: hidden;
  }
  .family-photo {
    position: absolute; left: 0; top: 0;
    width: 388px; height: 134px;
    background: linear-gradient(90deg, var(--photo-warm-a) 0%, #e2cbbb 45%, var(--photo-warm-b) 100%);
  }
  .brand {
    position: absolute; left: 388px; top: 0;
    width: 192px; height: 134px;
    display: flex; align-items: center; justify-content: center; gap: 8px;
    padding: 0 12px;
  }
  .brand-dot {
    width: 14px; height: 14px; border-radius: 50%;
    background: var(--gold); flex: none;
  }
  .brand-name {
    color: var(--blue); font-weight: 600; font-size: 13px;
    line-height: 1.3; letter-spacing: 0.3px;
  }
  .top-rule {
    position: absolute; left: 0; top: 134px;
    width: 100%; height: 7px; background: var(--blue);
  }
  .headline {
    position: absolute; left: 0; top: 164px; width: 100%;
    text-align: center; color: var(--blue);
    font-weight: 800; font-size: 27px; letter-spacing: 3.2px;
  }
  .tagline {
    position: absolute; left: 0; top: 200px; width: 100%;
    text-align: center; color: var(--gold);
    font-weight: 600; font-size: 17px; letter-spacing: 2.6px;
  }
  .seniors-photo {
    position: absolute; left: 0; top: 227px;
    width: 100%; height: 168px;
    background: linear-gradient(90deg, var(--photo-dark-a) 0%, var(--photo-dark-c) 30%, var(--photo-dark-b) 55%, var(--photo-dark-c) 75%, var(--photo-dark-a) 100%);
  }
  .no-word {
    position: absolute; left: 88px; top: 246px;
    color: var(--white); font-weight: 800; font-size: 104px;
    line-height: 1; letter-spacing: -2px;
  }
  .no-list {
    position: absolute; left: 266px; top: 270px;
    list-style: none; color: var(--white);
    font-weight: 500; font-size: 16px; line-height: 21px;
  }
  .no-list li::before { content: "·"; }
  .payout {
    position: absolute; left: 0; top: 413px; width: 100%;
    text-align: center; color: var(--blue);
    font-weight: 600; font-size: 15px; line-height: 20px; letter-spacing: 2.2px;
  }
  .cta-band {
    position: absolute; left: 0; top: 471px;
    width: 100%; height: 67px; background: var(--blue);
    display: flex; align-items: center; padding-left: 24px; gap: 12px;
    color: var(--white);
  }
  .cta-text {
    font-weight: 700; font-size: 13.5px; line-height: 18px; letter-spacing: 1.6px;
  }
  .cta-phone {
    font-weight: 700; font-size: 33px; letter-spacing: 2.4px; white-space: nowrap;
  }
  .footer-band {
    position: absolute; left: 0; top: 538px;
    width: 100%; height: 42px; background: var(--gold);
    display: flex; align-items: center; justify-content: center;
    color: var(--white); font-weight: 600; font-size: 11px; letter-spacing: 1px;
  }
</style>
</head>
<body>
  <main class="flyer">
    <div class="family-photo" role="img" aria-label="Smiling young family of four posed together on a white bed"></div>
    <div class="brand">
      <span class="brand-dot"></span>
      <span class="brand-name">Bluegate Financial Services, Inc.</span>
    </div>
    <div class="top-rule"></div>

    <h1 class="headline">REVERSE MORTGAGES</h1>
    <p class="tagline">YOUR ROAD TO FINANCIAL FREEDOM</p>

    <div class="seniors-photo" role="img" aria-label="Row of toned photos of smiling older adults"></div>
    <div class="no-word">NO</div>
    <ul class="no-list">
      <li>Monthly Payments</li>
      <li>Income Requirements</li>
      <li>Credit Score Requirements</li>
      <li>Loss of Ownership</li>
    </ul>

    <p class="payout">RECEIVE CASH BY LUMP SUM,<br>MONTHLY INSTALLMENTS OR A LINE OF CREDIT!!</p>

    <div class="cta-band">
      <p class="cta-text">CALL US TODAY FOR A<br>FREE CONSULTATION!!</p>
      <p class="cta-phone">(800) 471-2965</p>
    </div>
    <div class="footer-band">BLUEGATE FINANCIAL SERVICES, INC. NMLS #318760 | WWW.BLUEGATEHOME.COM</div>
  </main>
</body>
</html>
```